8-page brochure for laboratory equipment in the beverage can industry

We are a small company in the quality inspection and testing industry for beverage and food cans and are in need of a product brochure for one of our key products.The brochure should comprise of 8-pages. We will need both a print-ready format (which we would like to print on 2 double-sided A3 pages, then fold them), as well as an electronic version of the brochure (PDF). We also need to be able to make modifications to it, so we will need the open design file.We have corporate colors and fonts that will have to be used, which we will provide you with.The structure and content are defined, but we need some creative thinking to make it look great!

Target Market(s)

Beverage fillers

Font styles to use
Other font styles liked:
• Nexa Bold, Gotham Book, Calibri

Requirements
Must have
• Must be informative and look appealing.
• Must use the content from the Word document provided (better quality images will be provided if needed).
• Must use the company's corporate colors and fonts.
• Colors:
• Green: CMYK 99, 21, 86, 7
• Dark Grey: CMYK 67, 62, 58, 45
• Light Grey: CMYK 45, 36, 35, 1

```html
<!DOCTYPE html>
<html lang="en">
<head>
<meta charset="utf-8">
<title>Seam Measurement – Brochure Page 3</title>
<link href="https://fonts.googleapis.com/css2?family=Montserrat:wght@400;500;800&family=Saira+Semi+Condensed:wght@600&display=swap" rel="stylesheet">
<style>
  :root{
    --green:#00854f;
    --dark:#3b3633;
    --light:#8f8f91;
    --white:#ffffff;
    --ink:#1e1e1e;
  }
  *{margin:0;padding:0;box-sizing:border-box}
  html,body{width:846px;height:1200px;overflow:hidden;background:var(--white)}
  .page{position:relative;width:846px;height:1200px;font-family:"Montserrat",sans-serif;color:var(--ink)}
  .abs{position:absolute}
  .stripe{position:absolute;height:6px}
  .stripe.green{background:var(--green)}
  .stripe.dark{background:var(--dark)}
  .brand{position:absolute;left:487px;top:-4px;font-family:"Montserrat",sans-serif;font-weight:800;font-size:42px;letter-spacing:1px;color:var(--dark)}
  .tagline{position:absolute;left:523px;top:47px;font-size:13px;color:var(--light);letter-spacing:.3px}
  .section-bar{position:absolute;left:51px;width:743px;height:34px;background:var(--green)}
  .section-bar h2{font-family:"Saira Semi Condensed",sans-serif;font-weight:600;font-size:25px;color:var(--white);line-height:34px;padding-left:23px;letter-spacing:-.3px}
  .bullets{position:absolute;list-style:none;font-size:18.4px;line-height:24.2px}
  .bullets li{position:relative;padding-left:23px}
  .bullets li::before{content:"";position:absolute;left:2px;top:5px;width:12px;height:12px;border:2.4px solid var(--green);border-radius:50%}
  .figure{position:absolute}
  .caption{position:absolute;text-align:center;font-size:17px;line-height:22px}
  .footer-web{position:absolute;left:38px;top:1174px;font-size:13px;background:var(--white);padding:0 3px;color:var(--dark)}
  .page-no{position:absolute;left:784px;top:1160px;font-size:19px;color:var(--white)}
</style>
</head>
<body>
<div class="page">
  <!-- header -->
  <div class="stripe green" style="left:0;top:0;width:478px"></div>
  <div class="stripe dark" style="left:0;top:15px;width:478px"></div>
  <div class="stripe green" style="left:0;top:30px;width:478px"></div>
  <div class="stripe green" style="left:806px;top:0;width:40px"></div>
  <div class="stripe dark" style="left:806px;top:15px;width:40px"></div>
  <div class="stripe green" style="left:806px;top:30px;width:40px"></div>
  <div class="brand">NORVELT</div>
  <div class="tagline">QUALITY | ACCURACY | RELIABILITY</div>

  <div class="section-bar" style="top:71px"><h2>How does X-ray seam measurement work?</h2></div>

  <ul class="bullets" style="left:52px;top:112px;width:510px">
    <li>X-rays are sent through the seam sideways. A detector reads the remaining radiation. When X-rays are travelling through several layers of material, less radiation is going through the material, meaning that some percentage will be absorbed by the material depending on density. This results in a darker region within the image, which, in turn, allows a precise measurement of the individual layers of the seam.</li>
    <li>For a better understanding and visualization, the virtual seam image translates the X-ray image into a classic cross-section image.</li>
  </ul>

  <div class="figure" role="img" aria-label="Technical drawing of upper and lower X-ray beam angles across a can seam" style="left:573px;top:135px;width:218px;height:114px;border:1px solid #777;background:linear-gradient(#fbfbfb,#f1f1f1)"></div>
  <div class="figure" role="img" aria-label="Drawing of beam paths crossing a round can outline" style="left:580px;top:272px;width:210px;height:103px;background:radial-gradient(circle at 50% 50%,#fff 40%,#e9e9e9 42%,#fff 48%)"></div>

  <div class="caption" style="left:70px;top:412px;width:220px">X-Ray projection<br>(radial)</div>
  <div class="caption" style="left:322px;top:412px;width:228px">Conversion of X-Ray im-<br>age to „virtual seam“</div>
  <div class="caption" style="left:556px;top:412px;width:240px">Classic cross section view<br>(tangential)</div>

  <div class="figure" role="img" aria-label="Radial X-ray projection of seam layers" style="left:53px;top:467px;width:257px;height:140px;background:linear-gradient(90deg,#d9d9d9 0%,#444 10%,#333 35%,#1f1f1f 50%,#333 70%,#444 88%,#9a9a9a 100%)"></div>
  <div class="figure" role="img" aria-label="Virtual seam diagram with body hook, cover hook and overlap measurements" style="left:326px;top:467px;width:219px;height:140px;background:linear-gradient(#fff 20%,#3a3550 20%,#4a3434 55%,#3a3550 80%,#fff 80%)"></div>
  <div class="figure" role="img" aria-label="Tangential cross section image of a double seam" style="left:558px;top:469px;width:234px;height:139px;background:radial-gradient(ellipse at 45% 50%,#9a9a9a 0%,#555 35%,#141414 65%)"></div>

  <div class="figure" role="img" aria-label="360 degree seam scan strips with tightness colour map" style="left:223px;top:620px;width:350px;height:166px;background:repeating-linear-gradient(#e8e8e8 0,#e8e8e8 10px,#e8b58a 10px,#d7c7a0 20px,#e8e8e8 20px,#e8e8e8 26px);border-left:17px solid #eee;border-right:83px solid #f0f0f0"></div>

  <div class="section-bar" style="top:790px"><h2>Wrinkle rating with X-ray</h2></div>

  <ul class="bullets" style="left:52px;top:838px;width:280px">
    <li>Non-destructive wrinkle measurement</li>
    <li>360° scan of the can seam</li>
    <li>Automatic detection and calculation of tightness percentage</li>
    <li>Number of anomalies in the cover hook are clearly visible</li>
    <li>Leakers will be found thanks to the 360° scan</li>
  </ul>

  <div class="figure" role="img" aria-label="Wrinkle rating scan strips with percentage markings" style="left:468px;top:878px;width:326px;height:254px;background:repeating-linear-gradient(#fff 0,#fff 14px,#d9d9d9 14px,#7fb0e0 22px,#e03a2a 28px,#fff 36px)"></div>
  <div class="figure" role="img" aria-label="Close-up photograph of a can seam edge" style="left:329px;top:838px;width:180px;height:130px;background:linear-gradient(150deg,#cfd3e0 0%,#c0c4d4 35%,#a89a6a 48%,#cfd3e0 60%,#dfe2ea 100%)"></div>

  <!-- footer -->
  <svg class="abs" style="left:0;top:1150px" width="846" height="50" viewBox="0 0 846 50">
    <polygon points="690,2 846,2 846,50 610,50" fill="var(--green)"/>
    <rect x="0" y="16" width="700" height="7" fill="var(--green)"/>
    <polygon points="0,28 652,28 640,36 0,36" fill="var(--dark)"/>
    <rect x="0" y="43" width="846" height="7" fill="var(--green)"/>
  </svg>
  <div class="footer-web">www.norvelt-lab.com</div>
  <div class="page-no">3</div>
</div>
</body>
</html>
```